Banner poster with different motifs

I'm looking for 5 banners and posters in A1 format in the same design, or the similarity must be recognizable...
Kept quite simple with different titles.

1 ballet
2 Contemporary Dance
3 high heels
4 Salsa & Bachata & Zouk
5 Hip Hop

Modern bright colors
it is for the entrance so that the students see here is a dance school

The text may also be included in the image
The photos are for guidance only; some are our own, some are purchased. However, we are permitted to use them, including our logo, of course.

```html
<!DOCTYPE html>
<html lang="en">
<head>
<meta charset="utf-8">
<title>High Heels – Vivaro Dance Center</title>
<link rel="stylesheet" href="https://fonts.googleapis.com/css2?family=Montserrat:wght@300;800&family=Quicksand:wght@300;400&display=swap">
<style>
  :root {
    --stage: #7f7f7f;
    --ink: #141213;
    --smoke-deep: #0d3a52;
    --smoke: #1b6f99;
    --smoke-bright: #2a8fc2;
    --paper-text: #ffffff;
    --soft-text: #e6eef3;
  }
  * { margin: 0; padding: 0; box-sizing: border-box; }
  html, body {
    width: 1200px; height: 800px; overflow: hidden;
    background: var(--stage);
  }
  .canvas {
    position: relative; width: 1200px; height: 800px;
    display: flex; align-items: center; justify-content: center;
  }
  .poster {
    position: relative; width: 524px; height: 740px; overflow: hidden;
    background: var(--ink);
    font-family: "Quicksand", sans-serif; color: var(--paper-text);
  }
  .poster__photo {
    position: absolute; inset: 0;
    background:
      radial-gradient(ellipse 55% 45% at 62% 40%, rgba(42,143,194,.75), transparent 70%),
      radial-gradient(ellipse 60% 40% at 30% 78%, rgba(27,111,153,.8), transparent 70%),
      radial-gradient(ellipse 40% 30% at 80% 70%, rgba(13,58,82,.9), transparent 75%),
      linear-gradient(180deg, var(--ink) 0%, var(--smoke-deep) 45%, var(--smoke-deep) 75%, var(--ink) 100%);
  }
  .title {
    position: absolute; left: 0; top: 0;
    transform-origin: 0 0;
    white-space: nowrap; text-transform: uppercase;
    font-family: "Montserrat", sans-serif;
  }
  .title--heels {
    transform: translate(58px, 352px) rotate(-90deg);
    font-weight: 800; font-size: 62px; letter-spacing: 16px; line-height: 1;
  }
  .title--high {
    transform: translate(150px, 668px) rotate(-90deg);
    font-weight: 300; font-size: 76px; letter-spacing: 30px; line-height: 1;
    color: transparent; -webkit-text-stroke: 1.6px var(--paper-text);
  }
  .brand {
    position: absolute; top: 62px; right: 36px; width: 220px;
    display: flex; flex-direction: column; align-items: center;
  }
  .brand__mark {
    display: flex; align-items: center; gap: 12px;
  }
  .brand__dot {
    width: 28px; height: 28px; border: 1.5px solid var(--paper-text); border-radius: 50%;
  }
  .brand__name {
    font-weight: 300; font-size: 34px; letter-spacing: 4px; text-transform: uppercase;
  }
  .brand__line {
    margin-top: 30px; padding-bottom: 5px; width: 100%; text-align: center;
    font-weight: 300; font-size: 17px; letter-spacing: .5px; color: var(--soft-text);
    border-bottom: 1px solid rgba(255,255,255,.6);
  }
  .contact {
    position: absolute; left: 0; right: 0; bottom: 26px;
    display: flex; justify-content: space-between; align-items: flex-end;
    padding: 0 28px;
    font-weight: 300; font-size: 11.5px; letter-spacing: .3px; color: var(--soft-text);
  }
  .contact__phone { margin-bottom: 0; }
  .contact__mail { margin-bottom: 18px; }
  .contact__web { margin-bottom: 36px; }
</style>
</head>
<body>
  <main class="canvas">
    <article class="poster">
      <div class="poster__photo" role="img" aria-label="Photo of a dancer in a black two-piece and thigh-high platform boots, arms crossed above her head, against dark blue smoke"></div>

      <h1 class="title title--heels">Heels</h1>
      <p class="title title--high">High</p>

      <header class="brand">
        <div class="brand__mark">
          <span class="brand__dot"></span>
          <span class="brand__name">Vivaro</span>
        </div>
        <p class="brand__line">Vivaro Dance Center</p>
      </header>

      <footer class="contact">
        <span class="contact__phone">+49(0) 170 000 123 45</span>
        <span class="contact__mail">info@vivaro-dance.de</span>
        <span class="contact__web">www.vivaro-dance.de</span>
      </footer>
    </article>
  </main>
</body>
</html>
```